Poster Design for kebab shop products

need a new poster for our new blazer tray special, sign will be inside of shopping centre at different location to shop will need to stand out and draw customers to the store, MUST contain shops logo & picture added, poster size will be 76cm x 101cm so will need to suit that size

MUST ALSO CONTAIN THE FOLLOWING
Blazer Tray / HSP
Lamb & Chips
Chicken & Chips
Beef & Chips
+ Can $15

Target Market(s)

new customers

Industry/Entity Type

Retail

Font styles to use
Sans Serif

Colors

Designer to choose colors to be used in the design.

Requirements
Must have
• company logo
• picture of blazr tray provided
• Blazer Tray / HSP
• Lamb & Chips
• Chicken & Chips
• Beef & Chips
• + Can $15

```html
<!DOCTYPE html>
<html lang="en">
<head>
<meta charset="utf-8">
<title>Blazer Tray Special Poster</title>
<link href="https://fonts.googleapis.com/css2?family=Lilita+One&family=Roboto+Condensed:wght@700&family=Patrick+Hand&display=swap" rel="stylesheet">
<style>
  :root {
    --bg-deep: #3a0106;
    --bg-mid: #8e0a14;
    --bg-glow: #b3121c;
    --gold-light: #fbe08a;
    --gold: #e2aa2e;
    --gold-dark: #b27514;
    --cream: #f3e3b0;
    --cream-dark: #d2b36a;
    --title-shadow: #4a0a0a;
    --brand-red: #c0141c;
    --white: #ffffff;
    --ribbon: #f0901e;
    --badge-yellow: #fcd625;
    --badge-dark: #c8201e;
    --star-red: #e0151d;
    --food-brown: #6b3d1c;
    --food-gold: #e3b555;
    --foam: #f1f1ef;
  }
  * { box-sizing: border-box; margin: 0; padding: 0; }
  html, body { width: 774px; height: 1200px; overflow: hidden; }
  body { background: var(--bg-deep); }
  .poster {
    position: relative;
    width: 774px;
    height: 1200px;
    overflow: hidden;
    background: radial-gradient(ellipse 70% 55% at 50% 45%, var(--bg-glow) 0%, var(--bg-mid) 45%, var(--bg-deep) 100%);
    font-family: "Roboto Condensed", Arial, sans-serif;
  }
  .brand-rule {
    position: absolute;
    top: 50px;
    height: 2px;
    width: 150px;
    background: linear-gradient(90deg, transparent, rgba(255,255,255,0.75));
  }
  .brand-rule.left { left: 120px; }
  .brand-rule.right { right: 120px; transform: scaleX(-1); }
  .brand-card {
    position: absolute;
    left: 270px;
    top: -12px;
    width: 234px;
    height: 122px;
    background: var(--white);
    border-radius: 14px;
    display: flex;
    align-items: center;
    justify-content: center;
    gap: 10px;
    padding-top: 14px;
  }
  .brand-dot {
    width: 22px; height: 22px;
    border-radius: 50%;
    background: var(--ribbon);
  }
  .brand-name {
    font-family: "Lilita One", sans-serif;
    font-size: 34px;
    color: var(--brand-red);
    letter-spacing: 0.5px;
  }
  .title {
    position: absolute;
    left: 0; right: 0;
    text-align: center;
    font-family: "Lilita One", sans-serif;
    line-height: 1;
    filter: drop-shadow(3px 5px 0 var(--title-shadow)) drop-shadow(0 6px 10px rgba(0,0,0,0.45));
  }
  .title span {
    background-clip: text;
    -webkit-background-clip: text;
    color: transparent;
  }
  .title.line-one { top: 118px; font-size: 150px; }
  .title.line-one span { background-image: linear-gradient(180deg, var(--gold-light) 0%, var(--gold) 55%, var(--gold-dark) 100%); }
  .title.line-two { top: 250px; font-size: 150px; }
  .title.line-two span { background-image: linear-gradient(180deg, #fff6d6 0%, var(--cream) 50%, var(--cream-dark) 100%); }
  .product-photo {
    position: absolute;
    left: 132px;
    top: 440px;
    width: 570px;
    height: 490px;
    border-radius: 40px 40px 30px 30px;
    background: radial-gradient(ellipse 42% 36% at 50% 62%, var(--food-brown) 0%, #8a5a2a 45%, var(--food-gold) 68%, var(--foam) 72%, #dcdcd8 100%);
  }
  .special-badge {
    position: absolute;
    left: 322px;
    top: 452px;
    width: 170px;
    height: 80px;
  }
  .special-badge svg { position: absolute; inset: 0; }
  .special-badge .label {
    position: absolute;
    inset: 0 0 14px 0;
    display: flex;
    align-items: center;
    justify-content: center;
    font-family: "Roboto Condensed", sans-serif;
    font-weight: 700;
    font-size: 38px;
    color: #111;
    transform: rotate(-3deg);
  }
  .price-burst {
    position: absolute;
    left: 68px;
    top: 888px;
    width: 98px;
    height: 98px;
  }
  .price-burst svg { position: absolute; inset: 0; }
  .price-burst .price {
    position: absolute;
    inset: 0;
    display: flex;
    align-items: center;
    justify-content: center;
    font-family: "Lilita One", sans-serif;
    font-size: 36px;
    color: var(--white);
    transform: rotate(-6deg);
  }
  .price sup { font-size: 20px; margin-right: 1px; }
  .offer-ribbon {
    position: absolute;
    left: 106px;
    top: 994px;
    width: 556px;
    height: 60px;
  }
  .offer-ribbon svg { position: absolute; inset: 0; }
  .offer-ribbon .offer-name {
    position: absolute;
    inset: 0;
    display: flex;
    align-items: center;
    justify-content: center;
    font-family: "Patrick Hand", sans-serif;
    font-size: 40px;
    letter-spacing: 2px;
    color: var(--white);
  }
  .combo-list {
    position: absolute;
    left: 50px;
    top: 1068px;
    width: 674px;
    display: flex;
  }
  .combo {
    flex: 1;
    text-align: center;
    color: var(--white);
    font-size: 25px;
    line-height: 1.3;
    font-weight: 700;
    padding: 2px 0;
  }
  .combo + .combo { border-left: 1px solid rgba(255,255,255,0.45); }
</style>
</head>
<body>
  <main class="poster">
    <div class="brand-rule left"></div>
    <div class="brand-rule right"></div>
    <div class="brand-card">
      <span class="brand-dot"></span>
      <span class="brand-name">Grill Haven</span>
    </div>

    <h1 class="title line-one"><span>BLAZER</span></h1>
    <h1 class="title line-two"><span>TRAY</span></h1>

    <div class="product-photo" role="img" aria-label="Open foam takeaway box of chips topped with sliced kebab meat, garlic sauce and chilli sauce"></div>

    <div class="special-badge">
      <svg viewBox="0 0 170 80" aria-hidden="true">
        <polygon points="22,68 10,78 30,70" fill="var(--badge-dark)"/>
        <polygon points="14,14 166,6 160,58 6,70" fill="var(--badge-yellow)"/>
      </svg>
      <span class="label">SPECIAL</span>
    </div>

    <div class="price-burst">
      <svg viewBox="0 0 100 100" aria-hidden="true">
        <polygon fill="var(--star-red)" points="98,50 88.6,60.4 91.6,74 78.3,78.3 74,91.6 60.4,88.6 50,98 39.6,88.6 26,91.6 21.7,78.3 8.4,74 11.4,60.4 2,50 11.4,39.6 8.4,26 21.7,21.7 26,8.4 39.6,11.4 50,2 60.4,11.4 74,8.4 78.3,21.7 91.6,26 88.6,39.6"/>
      </svg>
      <span class="price"><sup>$</sup>15</span>
    </div>

    <div class="offer-ribbon">
      <svg viewBox="0 0 556 60" aria-hidden="true">
        <path d="M6,6 H550 L538,30 L550,54 H6 L18,30 Z" fill="rgba(0,0,0,0.15)" stroke="var(--ribbon)" stroke-width="3" stroke-linejoin="round"/>
      </svg>
      <span class="offer-name">SPECIAL BLAZER TRAY / HSP</span>
    </div>

    <section class="combo-list">
      <div class="combo">LAMB &amp; CHIPS<br>+ CAN</div>
      <div class="combo">CHICKEN &amp; CHIPS<br>+ CAN</div>
      <div class="combo">BEEF &amp; CHIPS<br>+ CAN</div>
    </section>
  </main>
</body>
</html>
```